Professional and creatice Life Coach - Business Card design

I just relaunched my website and now i a need a correspoonding business card for my task as life coach. My website is www.dlorvan.net as reference. The compass is kind of a symbol for my work, as I help people navigate through their challenging phases in life. The business card should be colorful, but not too playful as I also adress business people. So it sould be creative, but professional (also to suport my other business as Management Consultant)

Target Market(s)

People who want to get teir problems resolved, in business, partnership and other personal realms

Industry/Entity Type

Life Coaching

Contact Information for Business Card

Front side should include Name, Phone number, Email, Website and address

Font styles to use
Sans Serif

Colors
add136

Requirements
Must have
• "Mag. Benedikt Haufmoll" -> Name
"Energetische Praxis" -> Jobtitle (describing my profession as life coach)
colours and style should match my website www.dlorvan.net
Nice to have
• a compass as a symbol

```html
<!DOCTYPE html>
<html lang="de">
<head>
<meta charset="utf-8">
<title>Benedikt Haufmoll – Visitenkarte</title>
<link rel="stylesheet" href="https://fonts.googleapis.com/css2?family=Ubuntu:wght@400;500;700&display=swap">
<style>
  :root {
    --stage: #2b2d31;
    --lime: #add136;
    --lime-light: #c4e06a;
    --lime-deep: #9cc12a;
    --name-blue: #4a5a78;
    --accent-red: #c8242b;
    --ink: #3a3a3a;
    --muted: #6b6f5a;
    --ring: #2a2626;
  }
  * { margin: 0; padding: 0; box-sizing: border-box; }
  html, body { width: 1200px; height: 900px; overflow: hidden; }
  body {
    background: var(--stage);
    font-family: "Ubuntu", sans-serif;
    position: relative;
  }
  .card {
    position: absolute;
    left: 330px;
    width: 540px;
    height: 310px;
    border-radius: 24px;
    background: linear-gradient(135deg, var(--lime-deep) 0%, var(--lime-light) 45%, var(--lime) 100%);
    overflow: hidden;
  }
  .card--front { top: 110px; }
  .card--back { top: 480px; }

  .front__watermark {
    position: absolute;
    left: 110px;
    top: 70px;
    width: 200px;
    height: 200px;
    border-radius: 50%;
    border: 24px solid rgba(140, 170, 40, 0.28);
  }
  .front__identity { position: absolute; left: 32px; top: 30px; }
  .identity__name {
    font-size: 21px;
    font-weight: 700;
    color: var(--name-blue);
    letter-spacing: 0.2px;
  }
  .identity__surname { color: var(--accent-red); }
  .identity__role {
    font-size: 11px;
    color: var(--muted);
    margin-top: 2px;
  }
  .front__contact {
    position: absolute;
    left: 32px;
    top: 150px;
    list-style: none;
    font-size: 12.5px;
    color: var(--ink);
    font-weight: 500;
  }
  .contact__item {
    display: flex;
    align-items: center;
    gap: 8px;
    margin-bottom: 5px;
  }
  .contact__icon { width: 11px; height: 11px; flex: none; }
  .contact__highlight { color: var(--accent-red); }
  .front__address {
    position: absolute;
    right: 34px;
    bottom: 28px;
    text-align: right;
    font-size: 13.5px;
    font-weight: 700;
    color: var(--ink);
    line-height: 1.35;
  }

  .back__mark {
    position: absolute;
    left: 50%;
    top: 50%;
    transform: translate(-50%, -50%);
    display: flex;
    align-items: center;
    gap: 14px;
  }
  .back__circle {
    width: 70px;
    height: 70px;
    border-radius: 50%;
    border: 10px solid var(--ring);
  }
  .back__wordmark {
    font-size: 26px;
    font-weight: 700;
    color: var(--ring);
  }
</style>
</head>
<body>
  <section class="card card--front" aria-label="Vorderseite">
    <div class="front__watermark" aria-hidden="true"></div>

    <header class="front__identity">
      <h1 class="identity__name">Mag. Benedikt <span class="identity__surname">Haufmoll</span></h1>
      <p class="identity__role">Energetische Praxis</p>
    </header>

    <ul class="front__contact">
      <li class="contact__item">
        <svg class="contact__icon" viewBox="0 0 12 12" aria-hidden="true">
          <rect x="3" y="0.5" width="6" height="11" rx="1.2" fill="none" stroke="var(--accent-red)" stroke-width="1.4"/>
          <circle cx="6" cy="9.4" r="0.8" fill="var(--accent-red)"/>
        </svg>
        <span>+43 660 4817392</span>
      </li>
      <li class="contact__item">
        <svg class="contact__icon" viewBox="0 0 12 12" aria-hidden="true">
          <rect x="0.5" y="2" width="11" height="8" rx="1" fill="var(--accent-red)"/>
          <path d="M1 2.6 L6 6.6 L11 2.6" fill="none" stroke="#fff" stroke-width="1"/>
        </svg>
        <span>office@dlorvan.net</span>
      </li>
      <li class="contact__item">
        <svg class="contact__icon" viewBox="0 0 12 12" aria-hidden="true">
          <circle cx="6" cy="6" r="5.3" fill="none" stroke="var(--accent-red)" stroke-width="1.3"/>
          <ellipse cx="6" cy="6" rx="2.3" ry="5.3" fill="none" stroke="var(--accent-red)" stroke-width="1"/>
          <line x1="0.8" y1="6" x2="11.2" y2="6" stroke="var(--accent-red)" stroke-width="1"/>
        </svg>
        <span>www.<span class="contact__highlight">dlorvan</span>.net</span>
      </li>
    </ul>

    <address class="front__address" style="font-style: normal;">
      Ahornweg 9,<br>4820 Bad Feldau, Austria
    </address>
  </section>

  <section class="card card--back" aria-label="Rückseite">
    <div class="back__mark">
      <div class="back__circle" aria-hidden="true"></div>
      <span class="back__wordmark">Benedikt Haufmoll</span>
    </div>
  </section>
</body>
</html>
```